Real Estate Office Front Facade Redesign - ideas needed

Kindly read this brief thoroughly as there are 2 deliverables:
1. Office building façade redesign (see attached logo and also photo of our office building façade)
2. I also require a design for a freestanding signboard that will be coordinated with the design of the office front please see the images attached labelled signboard.

Deliverable number 1:
I am looking for a minimalist contemporary design with strong colours to draw the attention of the passing Traffic.

The office facade is to be repainted so you may choose to recolour the office in any way to coordinate with logo however the attached logo must remain as is. I prefer the colours red black and white or shades of these colours.

Quillon property managers is a new company looking to target property investors in the local area. Most of our clients are from a middle to upper income demographic. We help these investors to rent out their properties and ensure they are maintained in good condition and provide a regular income.

The area we operate in is centrally located and close to the central business district of Perth.

Our office is situated in a residential area on a busy road facing diagonally at 45° down the road. People see our office from their cars whilst driving to work, there is no pedestrian traffic in the area. Therefore the office façade needs to stand out and any signage must be read by quickly passing traffic or convey our brand in seconds. Whilst the view of the office from the road is obscured somewhat by trees from a distance, once within 50 to 100 m of the office the full face of the office front is visible facing directly at the driver.

No measurements are provided for the façade of the office (please see the photo provided), this is a blank canvas as the whole building will be repainted to fit in with YOUR design. A logo is also attached. The colours red black and white are preferred.

Please provide an image of the office with signage/colours superimposed.

Deliverable number 2:
Also attached is an image of a freestanding sign for which I require a design. This sign is used for advertising properties for lease or sale which will be erected outside the front of residential houses. Again this sign needs to be bold and bright with a contemporary design. It needs to stand out from the crowd of many other signs in the area, whilst the sign advertises the property it must also promote our company brand by having a prominent logo. The size of these signboards will either be 1250 mm x 900 mm or 1800 mm x 625 mm. Please note that this sign must be rectangular in shape and cannot have any text or logo protruding outside of the lines of the rectangular sign due to cost restrictions.

Target Market(s)

Industry/Entity Type

Real Estate

Font styles to use
Sans Serif

Colors
ec1f27
ffffff
000000

Requirements
Must have
• Contemporary uncluttered design using the colours red black and white of shades of.
Nice to have
• A prominent logo with the words "Property Managers" easily read by passing traffic.
• Files provided with editable text and the name of the font used.
Should not have
• designs protruding outside of the overall building facia or sign rectangle.

```html
<!DOCTYPE html>
<html lang="en">
<head>
<meta charset="utf-8">
<title>Quillon Property Managers – Office Facade and Signboard</title>
<link rel="stylesheet" href="https://fonts.googleapis.com/css2?family=Montserrat:wght@300;400&family=Roboto+Condensed:wght@300;400&display=swap">
<style>
  :root {
    --brand-red: #ec1f27;
    --ink: #000000;
    --facade: #0f1420;
    --wordmark: #2a2a2c;
    --white: #ffffff;
    --soffit: #e8e9eb;
    --glass: #c9cfd2;
    --frame: #f2f2f2;
    --backdrop: #ececec;
    --panel-grey: #e4e4e4;
    --timber: #d8b57a;
  }
  * { margin: 0; padding: 0; box-sizing: border-box; }
  html, body { width: 1200px; height: 841px; overflow: hidden; background: var(--backdrop); }
  .canvas { position: relative; width: 1200px; height: 841px; font-family: "Montserrat", sans-serif; }

  /* Fascia sign */
  .fascia {
    position: absolute; left: 82px; top: 62px; width: 1088px; height: 134px;
    background: var(--white);
    display: flex; align-items: center; justify-content: center; gap: 22px;
  }
  .brand-square { width: 62px; height: 62px; background: var(--brand-red); flex: none; }
  .brand-lockup { text-align: center; color: var(--wordmark); }
  .brand-name { font-weight: 400; font-size: 64px; letter-spacing: 12px; line-height: 1; }
  .brand-tagline { font-weight: 400; font-size: 16px; letter-spacing: 4px; margin-top: 8px; line-height: 1.2; }

  /* Awning band */
  .awning {
    position: absolute; left: 12px; top: 196px; width: 1188px; height: 68px;
    background: var(--facade);
    display: flex; align-items: center; justify-content: center;
  }
  .awning-url { color: var(--white); font-weight: 300; font-size: 48px; letter-spacing: 1px; line-height: 1; }
  .soffit { position: absolute; left: 70px; top: 264px; width: 1130px; height: 28px; background: var(--soffit); }

  /* Wall */
  .wall { position: absolute; left: 88px; top: 292px; width: 1100px; height: 345px; background: var(--facade); }
  .window { position: absolute; background: var(--glass); border: 8px solid var(--frame); }
  .window--left { left: 66px; top: 110px; width: 310px; height: 160px; }
  .window--mid { left: 482px; top: 118px; width: 180px; height: 140px; }
  .window--right { left: 840px; top: 118px; width: 180px; height: 140px; }
  .doors { position: absolute; left: 672px; top: 126px; width: 160px; height: 185px; border: 4px solid #2b2f38; background: #1d222c; }
  .wall-mark { position: absolute; left: 285px; top: 22px; width: 210px; height: 210px; background: var(--brand-red); opacity: .92; }

  .wall-sign {
    position: absolute; left: 760px; top: 325px; width: 157px; height: 80px;
    background: var(--panel-grey);
    display: flex; flex-direction: column; align-items: center; justify-content: center; gap: 4px;
    color: var(--wordmark);
  }
  .wall-sign .brand-square { width: 20px; height: 20px; }
  .wall-sign .brand-name { font-size: 19px; letter-spacing: 3px; }
  .wall-sign .brand-tagline { font-size: 6px; letter-spacing: 1px; margin-top: 1px; }

  /* Freestanding signboard */
  .signboard-frame { position: absolute; left: 548px; top: 495px; width: 200px; height: 330px; }
  .signboard-leg { position: absolute; top: 0; width: 14px; height: 330px; background: var(--timber); }
  .signboard-leg--left { left: 0; }
  .signboard-leg--right { right: 0; }
  .signboard {
    position: absolute; left: 562px; top: 500px; width: 172px; height: 264px;
    background: var(--white); display: flex; flex-direction: column; align-items: center;
    padding-top: 18px; color: var(--wordmark); box-shadow: 0 0 0 1px #d6d6d6;
  }
  .signboard .brand-square { width: 32px; height: 32px; }
  .signboard .brand-name { font-size: 25px; letter-spacing: 3px; margin-top: 10px; }
  .signboard .brand-tagline { font-size: 6.5px; letter-spacing: 1.2px; margin-top: 4px; }
  .signboard-rule { width: 130px; height: 1px; background: #bbbbbb; margin: 12px 0 8px; }
  .listing-status { font-family: "Roboto Condensed", sans-serif; font-weight: 300; color: var(--brand-red); font-size: 29px; }
  .listing-contact { font-family: "Roboto Condensed", sans-serif; font-size: 13px; line-height: 1.5; text-align: center; margin-top: 12px; color: var(--ink); }
  .signboard-footer {
    margin-top: auto; width: 100%; height: 34px; background: var(--ink);
    color: var(--white); font-family: "Roboto Condensed", sans-serif; font-size: 11px;
    display: flex; align-items: center; justify-content: center;
  }
</style>
</head>
<body>
<main class="canvas">
  <header class="fascia">
    <span class="brand-square" aria-hidden="true"></span>
    <div class="brand-lockup">
      <div class="brand-name">QUILLON</div>
      <div class="brand-tagline">PROPERTY MANAGERS</div>
    </div>
  </header>

  <div class="awning"><span class="awning-url">www.quillonproperty.com.au</span></div>
  <div class="soffit"></div>

  <section class="wall" aria-label="Repainted office front">
    <div class="window window--left"></div>
    <div class="window window--mid"></div>
    <div class="window window--right"></div>
    <div class="doors"></div>
    <div class="wall-mark" aria-hidden="true"></div>
  </section>

  <div class="wall-sign">
    <span class="brand-square" aria-hidden="true"></span>
    <div class="brand-name">QUILLON</div>
    <div class="brand-tagline">PROPERTY MANAGERS</div>
  </div>

  <div class="signboard-frame" aria-hidden="true">
    <span class="signboard-leg signboard-leg--left"></span>
    <span class="signboard-leg signboard-leg--right"></span>
  </div>
  <article class="signboard">
    <span class="brand-square" aria-hidden="true"></span>
    <div class="brand-name">QUILLON</div>
    <div class="brand-tagline">PROPERTY MANAGERS</div>
    <div class="signboard-rule"></div>
    <div class="listing-status">FOR LEASE</div>
    <div class="listing-contact">MOBILE: 0400 000 000<br>Office: 9412 3780</div>
    <div class="signboard-footer">www.quillonproperty.com.au</div>
  </article>
</main>
</body>
</html>
```